VO!REELS WEBSITE

I need to get the design for the website of my company, which is a production company based in Los Angeles called VO! REELS. The company works as a liason between Russian speaking and English speaking film communities, providing the spectrum of production services in Eastern Europe and United States of America.
Has to have the following links:
About
Locations
Works
I'd like to see the designs on the white background using the blue and red colors.
Please try to use the font of an old typewriter if you can. You can also get some ideas after looking at the logo, which you need to intergrate into the webdesign anyway.
Thank you very much and I wish you some inspiration!
Updates

I'd like to extend the project till July the 10th, please send more submissions

Reason: I want to give more time to make changes to my comments

Target Market(s)

Production studios from different countries, Directors, Producers, Clients

Industry/Entity Type

It Company

Font styles to use
Sans Serif
Other font styles liked:
• typewriter

Requirements
Must have
• Visible logo design intergrated into graphics

```html
<!DOCTYPE html>
<html lang="en">
<head>
<meta charset="utf-8">
<title>VO! REELS — Works</title>
<link rel="stylesheet" href="https://fonts.googleapis.com/css2?family=Special+Elite&display=block">
<style>
  :root {
    --white: #ffffff;
    --black: #000000;
    --ink: #3a3a3a;
    --brand-red: #c0202f;
    --brand-blue: #1e6fa8;
    --link-blue: #1a8fe0;
    --glow-blue: #3a9de0;
    --footer-text: #e6e6e6;
    --crew-grey: #1b1b1b;
  }
  * { margin: 0; padding: 0; box-sizing: border-box; }
  html, body {
    width: 1200px; height: 750px; overflow: hidden;
    background: var(--black);
    font-family: "Special Elite", "Courier New", monospace;
  }
  .page { position: relative; width: 1200px; height: 750px; background: var(--black); }

  .site-header {
    position: absolute; left: 0; top: 0; width: 1200px; height: 145px;
    background: var(--white);
  }
  .brand {
    position: absolute; left: 150px; top: 50px;
    display: flex; align-items: center; gap: 12px;
    font-size: 50px; line-height: 1; color: var(--brand-red);
    white-space: nowrap;
  }
  .brand-mark { width: 20px; height: 20px; border-radius: 50%; background: var(--brand-blue); flex: none; }
  .brand-underline {
    position: absolute; left: 104px; top: 181px; width: 342px; height: 2px;
    background: linear-gradient(90deg, transparent, var(--glow-blue) 35%, #7fc4f5 50%, var(--glow-blue) 65%, transparent);
  }

  .main-nav { position: absolute; top: 114px; left: 0; width: 1200px; height: 31px; }
  .nav-link {
    position: absolute; top: 0; font-size: 19px; color: var(--ink);
    text-decoration: none; line-height: 24px; white-space: nowrap;
  }
  .nav-link.home { left: 647px; }
  .nav-link.about { left: 738px; }
  .nav-link.locations { left: 838px; }
  .nav-link.works { left: 983px; }
  .nav-link.is-active::after {
    content: ""; position: absolute; left: 0; top: 26px; width: 60px; height: 5px;
    background: var(--brand-red);
  }

  .crew-backdrop {
    position: absolute; left: 770px; top: 262px; width: 430px; height: 330px;
    background:
      linear-gradient(180deg, rgba(0,0,0,0) 0%, rgba(0,0,0,0) 70%, var(--black) 100%),
      linear-gradient(90deg, var(--black) 0%, rgba(0,0,0,0) 30%),
      linear-gradient(160deg, #141414 0%, var(--crew-grey) 45%, #121212 100%);
    border-radius: 40px 40px 0 0;
  }

  .works-title {
    position: absolute; left: 149px; top: 289px;
    font-size: 24px; font-weight: normal; color: var(--link-blue);
    text-decoration: underline; text-underline-offset: 4px; white-space: nowrap;
  }

  .work-tile {
    position: absolute; width: 196px; height: 196px;
    border: 3px solid var(--white);
  }
  .work-tile.one {
    left: 159px; top: 354px;
    background:
      radial-gradient(circle at 55% 30%, #e0e0e0 0%, #8a8a8a 18%, rgba(40,40,40,0) 34%),
      radial-gradient(circle at 55% 72%, #d6d6d6 0%, #7a7a7a 18%, rgba(40,40,40,0) 34%),
      linear-gradient(90deg, #3a3a3a 0%, #6f6f6f 40%, #9a9a9a 75%, #cfcfcf 100%);
  }
  .work-tile.two {
    left: 412px; top: 354px;
    background:
      radial-gradient(circle at 8% 92%, #f3b9a0 0%, #f0c4ad 14%, rgba(240,196,173,0) 16%),
      linear-gradient(180deg, rgba(0,0,0,0) 82%, #3f4a56 84%, #e6e2cf 90%, #3f4a56 94%, #cfcabb 100%),
      radial-gradient(ellipse at 88% 60%, #2f3440 0%, #404652 22%, rgba(64,70,82,0) 36%),
      linear-gradient(135deg, #f1eed6 0%, #ecebcd 60%, #e6e2c4 100%);
  }
  .work-tile.three {
    left: 664px; top: 352px;
    background:
      radial-gradient(ellipse at 42% 55%, #8fb3b4 0%, #5a8288 25%, rgba(60,95,102,0) 45%),
      radial-gradient(ellipse at 82% 40%, #b54a4a 0%, rgba(181,74,74,0) 18%),
      linear-gradient(135deg, #d9e7e8 0%, #9fbcc0 35%, #3e6068 70%, #22383f 100%);
  }

  .site-footer {
    position: absolute; left: 0; top: 713px; width: 1200px; text-align: center;
    font-size: 12px; color: var(--footer-text);
  }
</style>
</head>
<body>
<div class="page">
  <header class="site-header">
    <div class="brand"><span class="brand-mark"></span><span class="brand-name">VO! REELS</span></div>
    <nav class="main-nav">
      <a class="nav-link home" href="#">Home</a>
      <a class="nav-link about" href="#">About</a>
      <a class="nav-link locations" href="#">Locations</a>
      <a class="nav-link works is-active" href="#">Works</a>
    </nav>
  </header>
  <div class="brand-underline"></div>

  <div class="crew-backdrop" role="img" aria-label="Faint silhouette of a film crew with camera and studio lights"></div>

  <main>
    <h1 class="works-title">VO! REELS WORKS</h1>
    <div class="work-tile one" role="img" aria-label="Black and white close-up of a vintage twin-lens camera"></div>
    <div class="work-tile two" role="img" aria-label="Vintage camera on a stack of books beside a pink telephone"></div>
    <div class="work-tile three" role="img" aria-label="Rolls of film canisters in teal tones"></div>
  </main>

  <footer class="site-footer">copyright all rights reserved - 2014</footer>
</div>
</body>
</html>
```